Website for an interior designer

We need a new website for Clara Beth Holloway whose new business name is Clara Beth Holloway Interiors. She is a residential interior designer with a mix of modern and contemporary tastes. We are in the process of overhauling her website which is +15 years old and not an accurate reflection of her tastes. The uploaded photos are from some of the houses she has done as well as her logo(s). We would need a section for "About Us" that would have a paragraph of text and bullets showing services and a gallery for photos (~12 total, more to come). A contract page would be optional. The client likes the feel/look of this website: https://www.pondrickstudio.example/ but doesn't want to copy it exactly.

Target Market(s)

Upscale home owners

Industry/Entity Type

Interior Design

Coding

Coded - Design and coding required

Number of Pages Required

4 page

Colors

Designer to choose only greyscale colors for use in the design.

Requirements
Must have
• Home page, about us page, gallery page, contact us page.

```html
<!DOCTYPE html>
<html lang="en">
<head>
<meta charset="utf-8">
<title>Clara Beth Holloway Interiors</title>
<link rel="stylesheet" href="https://fonts.googleapis.com/css2?family=Cinzel:wght@400;500&family=Montserrat:wght@400;500&family=Great+Vibes&display=swap">
<style>
:root{
  --bg-header:#3b3c3d;
  --bg-main:#424344;
  --bg-dark:#353637;
  --bg-card:#232323;
  --bg-team:#3a3b3c;
  --text:#ffffff;
  --text-soft:#d6d6d6;
  --text-muted:#b9b9b9;
  --accent:#dba597;
  --line:#6a6b6c;
}
*{margin:0;padding:0;box-sizing:border-box}
html,body{width:1200px;height:4000px;overflow:hidden}
body{position:relative;background:var(--bg-main);color:var(--text);font-family:"Montserrat",sans-serif}
.abs{position:absolute}
.serif{font-family:"Cinzel",serif}
.section-title{position:absolute;left:0;width:1200px;text-align:center;font-family:"Cinzel",serif;font-size:31px;letter-spacing:1px;font-weight:400}
.title-rule{position:absolute;left:580px;width:40px;height:2px;background:var(--accent)}
.btn{position:absolute;border:1px solid #9a9a9a;border-top:none;border-left:none;font-size:13px;letter-spacing:.5px;display:flex;align-items:center;justify-content:center;color:var(--text)}
.btn span{position:absolute;left:-4px;top:-4px;right:4px;bottom:4px;background:#2f3030;display:flex;align-items:center;justify-content:center;box-shadow:0 2px 6px rgba(0,0,0,.3)}
.pager{position:absolute;left:560px;width:80px;height:24px}

/* header */
.site-header{top:0;left:0;width:1200px;height:98px;background:var(--bg-header)}
.brand{left:140px;top:12px;width:190px;text-align:center}
.brand-mark{width:36px;height:36px;border:1px solid var(--text-soft);border-radius:50%;margin:0 auto 6px}
.brand-name{font-family:"Cinzel",serif;font-size:14px;letter-spacing:1px;line-height:1.2}
.main-nav{top:38px;font-family:"Cinzel",serif;font-size:13px;letter-spacing:1px}
.main-nav.active{color:var(--accent)}
.nav-underline{left:538px;top:90px;width:46px;height:2px;background:var(--accent)}

/* hero */
.hero{top:98px;left:0;width:1200px;height:572px;background:linear-gradient(100deg,#2a2a2b 0%,#3c3b39 40%,#5c5a56 70%,#807c76 100%)}
.hero-line1{top:312px;left:336px;font-family:"Cinzel",serif;font-size:23px}
.hero-script{top:300px;left:600px;font-family:"Great Vibes",cursive;font-size:78px;line-height:1}
.hero-a{top:348px;left:602px;font-family:"Great Vibes",cursive;font-size:40px}
.hero-line2{top:400px;left:548px;font-family:"Cinzel",serif;font-size:51px}

/* about */
.about-pattern{left:141px;top:742px;width:356px;height:422px;background:repeating-linear-gradient(135deg,#4a4b4c 0 2px,#3e3f40 2px 4px)}
.about-photo{left:180px;top:672px;width:356px;height:458px;background:linear-gradient(160deg,#8b8a86,#cfcac2 55%,#6f6b66)}
.about-title{left:576px;top:752px;font-family:"Cinzel",serif;font-size:25px}
.about-rule{left:577px;top:805px;width:40px;height:2px;background:var(--accent)}
.about-text{left:576px;top:825px;width:482px;font-size:13.5px;line-height:24px;color:var(--text-soft)}
.about-text p{margin-bottom:8px}

/* services */
.services-band{top:1250px;left:0;width:1200px;height:341px;background:var(--bg-dark)}
.service-card{top:1415px;width:302px;height:345px;background:var(--bg-card)}
.service-img{position:absolute;left:0;top:0;width:302px;height:242px}
.service-rule{position:absolute;left:12px;top:270px;width:22px;height:2px;background:var(--text-soft)}
.service-name{position:absolute;left:44px;top:260px;font-size:14.5px;line-height:19px;color:var(--text-soft)}
.service-link{position:absolute;left:44px;top:310px;font-size:11px;color:var(--accent);text-decoration:underline}
.service-num{position:absolute;right:10px;top:260px;font-size:34px;color:#4d4d4d;font-weight:400}

/* how it works */
.step{top:1994px;width:220px}
.step-icon{width:60px;height:56px}
.step-name{margin-top:30px;font-family:"Cinzel",serif;font-size:15px;letter-spacing:1px}
.step-text{margin-top:10px;font-size:12px;line-height:17px;color:var(--text-muted)}
.step-arrow{top:2010px;width:40px;height:24px}

/* cta */
.cta{top:2294px;left:0;width:1200px;height:371px;background:linear-gradient(90deg,#4e4e4e,#555452 50%,#3e3e3f)}

/* gallery */
.gallery-item{top:2834px;height:183px}

/* team */
.team{top:3161px;left:0;width:1200px;height:533px;background:var(--bg-team)}
.team-photo{top:3331px;width:213px;height:226px}
.team-card{top:3508px;width:202px;height:97px;background:#4a4a4b;padding:30px 0 0 30px}
.team-name{font-family:"Cinzel",serif;font-size:16px;letter-spacing:1px}
.team-role{margin-top:10px;font-size:13px;color:var(--text-soft)}

/* footer */
.site-footer{top:3694px;left:0;width:1200px;height:306px;background:var(--bg-dark)}
.foot-nav{top:3736px;font-family:"Cinzel",serif;font-size:13px;letter-spacing:1px}
.foot-nav.active{color:var(--accent)}
.foot-rule{left:141px;width:918px;height:1px;background:#4e4f50}
.contact-col{top:3830px;text-align:center;font-size:12px;line-height:17px;color:var(--text-soft)}
.contact-col strong{font-weight:500;color:var(--text)}
.contact-divider{top:3815px;width:1px;height:110px;background:#4e4f50}
.copyright{left:141px;top:3962px;font-size:11px;color:var(--text-soft)}
.copyright b{color:var(--accent);font-weight:400}
.social{top:3956px;width:24px;height:24px;border-radius:50%}
</style>
</head>
<body>

<header class="abs site-header">
  <div class="abs brand">
    <div class="brand-mark"></div>
    <div class="brand-name">Clara Beth Holloway Interiors</div>
  </div>
  <nav>
    <div class="abs main-nav active" style="left:538px">HOME</div>
    <div class="abs main-nav" style="left:628px">ABOUT US</div>
    <div class="abs main-nav" style="left:746px">SERVICES</div>
    <div class="abs main-nav" style="left:858px">GALLERY</div>
    <div class="abs main-nav" style="left:965px">CONTACT US</div>
  </nav>
  <div class="abs nav-underline"></div>
</header>

<section class="abs hero" role="img" aria-label="Photo of a dark modern living room with a leather sofa and pendant lights"></section>
<div class="abs hero-line1">GIVE YOUR LIVING ROOM</div>
<div class="abs hero-a">a</div>
<div class="abs hero-script" style="left:648px">New</div>
<div class="abs hero-line2">MAKE OVER</div>
<svg class="abs" style="left:88px;top:370px" width="34" height="28" viewBox="0 0 34 28" fill="none" stroke="#d9d9d9" stroke-width="2"><path d="M16 2 4 14l12 12M30 2 18 14l12 12"/></svg>
<svg class="abs" style="left:1068px;top:370px" width="46" height="28" viewBox="0 0 46 28" fill="none" stroke="var(--accent)" stroke-width="2"><path d="M2 2l12 12L2 26M16 2l12 12-12 12M30 2l12 12-12 12"/></svg>

<section aria-label="About">
  <div class="abs about-pattern"></div>
  <div class="abs about-photo" role="img" aria-label="Photo of the designer with clients reviewing a tablet in a furniture showroom"></div>
  <h2 class="abs about-title">ABOUT CLARA BETH HOLLOWAY</h2>
  <div class="abs about-rule"></div>
  <div class="abs about-text">
    <p>Clara Beth Holloway has extensive experience in all aspects of interior design. She has worked on a wide array of residential and commercial projects in her hometown of Houston and across the United States. Clara Beth’s taste can best be described as a sophisticated blend of modern and traditional styles that combine to create a clean, timeless space.</p>
    <p>Lorem ipsum dolor sit amet, consectetuer adipiscing elit, sed diam nonummy nibh euismod tincidunt ut laoreet dolore magna aliquam erat volutpat. Ut wisi enim ad minim veniam, quis nostrud exerci tation ullamcorper suscipit lobortis nisl ut aliquip ex ea.</p>
  </div>
  <div class="btn" style="left:581px;top:1075px;width:117px;height:40px"><span>READ MORE</span></div>
</section>

<section aria-label="Services">
  <div class="abs services-band"></div>
  <h2 class="section-title" style="top:1325px">OUR SERVICES</h2>
  <div class="title-rule" style="top:1377px"></div>

  <div class="abs service-card" style="left:141px">
    <div class="service-img" role="img" aria-label="Photo of design plans, swatches and a laptop on a desk" style="background:linear-gradient(135deg,#6f5a45,#c9b8a2 50%,#8a6f55)"></div>
    <div class="service-rule"></div>
    <div class="service-name">Concept Origination and<br>Project Management</div>
    <div class="service-link">READ MORE</div>
    <div class="service-num">01</div>
  </div>
  <div class="abs service-card" style="left:448px">
    <div class="service-img" role="img" aria-label="Photo of paint-splattered stairs in a bright hallway" style="background:linear-gradient(160deg,#d9c9a0,#b3564e 50%,#c86aa2)"></div>
    <div class="service-rule"></div>
    <div class="service-name">Selection of Paints, Finishes<br>and Construction Materials</div>
    <div class="service-link">READ MORE</div>
    <div class="service-num">02</div>
  </div>
  <div class="abs service-card" style="left:757px">
    <div class="service-img" role="img" aria-label="Photo of a meeting with a presenter at a whiteboard" style="background:linear-gradient(135deg,#d8dadd,#eeeeee 45%,#4b5261)"></div>
    <div class="service-rule"></div>
    <div class="service-name">Vendor Coordination<br>and Recommendations</div>
    <div class="service-link">READ MORE</div>
    <div class="service-num">03</div>
  </div>

  <svg class="pager" style="top:1798px" viewBox="0 0 80 24" fill="none" stroke-width="1.5"><path d="M14 4 6 12l8 8M22 4l-8 8 8 8" stroke="#888"/><path d="M46 4l8 8-8 8M56 4l8 8-8 8M66 4l8 8-8 8" stroke="var(--accent)"/></svg>
</section>

<section aria-label="How it works">
  <h2 class="section-title" style="top:1897px">HOW IT WORKS</h2>
  <div class="title-rule" style="top:1949px"></div>

  <div class="abs step" style="left:141px">
    <svg class="step-icon" viewBox="0 0 60 56" fill="none" stroke="#fff" stroke-width="2"><rect x="2" y="2" width="56" height="50"/><path d="M2 20h18V2M20 34h14v18M40 34h18"/><circle cx="46" cy="43" r="4"/></svg>
    <div class="step-name">DESIGN PROCESS</div>
    <div class="step-text">Lorem ipsum dolor sit amet couer adipiscing elit sed diam nonmy.</div>
  </div>
  <svg class="abs step-arrow" style="left:305px" viewBox="0 0 40 24" fill="none" stroke="#666" stroke-width="2"><path d="M2 12h34M26 3l10 9-10 9"/></svg>

  <div class="abs step" style="left:380px">
    <svg class="step-icon" viewBox="0 0 60 56" fill="none" stroke="#fff" stroke-width="2"><rect x="2" y="8" width="46" height="46"/><path d="M20 40l30-32 6 6-30 32-8 2z"/><path d="M8 48h10"/></svg>
    <div class="step-name">SUPERVISION</div>
    <div class="step-text">Lorem ipsum dolor sit amet couer adipiscing elit sed diam nonmy.</div>
  </div>
  <svg class="abs step-arrow" style="left:570px" viewBox="0 0 40 24" fill="none" stroke="#666" stroke-width="2"><path d="M2 12h34M26 3l10 9-10 9"/></svg>

  <div class="abs step" style="left:639px">
    <svg class="step-icon" viewBox="0 0 60 56" fill="none" stroke="#fff" stroke-width="2"><circle cx="34" cy="30" r="18" fill="#5a5656" stroke="none"/><rect x="2" y="2" width="34" height="52"/><path d="M2 2l22 6v46"/><circle cx="18" cy="30" r="2" fill="#fff"/></svg>
    <div class="step-name">BUDGET PLANNING</div>
    <div class="step-text">Lorem ipsum dolor sit amet couer adipiscing elit sed diam nonmy.</div>
  </div>
  <svg class="abs step-arrow" style="left:808px" viewBox="0 0 40 24" fill="none" stroke="#666" stroke-width="2"><path d="M2 12h34M26 3l10 9-10 9"/></svg>

  <div class="abs step" style="left:858px">
    <svg class="step-icon" viewBox="0 0 60 56" fill="none" stroke="#fff" stroke-width="2"><path d="M4 14 14 2h32l10 12z"/><rect x="6" y="14" width="48" height="40"/><path d="M6 24h48M24 54V38h12v16"/><rect x="12" y="30" width="8" height="6"/><rect x="40" y="30" width="8" height="6"/></svg>
    <div class="step-name">BUILD A HOME FOR YOU</div>
    <div class="step-text">Lorem ipsum dolor sit amet couer adipiscing elit sed diam nonmy.</div>
  </div>

  <div class="btn" style="left:539px;top:2172px;width:126px;height:36px"><span>GET STARTED</span></div>
</section>

<section aria-label="Call to action">
  <div class="abs cta" role="img" aria-label="Photo of an architect's hands over a model of a modern house"></div>
  <h2 class="section-title" style="top:2420px;font-size:40px">DO YOU WANT TO WORK WITH US?</h2>
  <div class="btn" style="left:536px;top:2500px;width:136px;height:36px"><span>CALL US TODAY</span></div>
</section>

<section aria-label="Gallery">
  <h2 class="section-title" style="top:2741px">WORK GALLERY</h2>
  <div class="title-rule" style="top:2793px"></div>
  <div class="abs gallery-item" style="left:141px;width:213px;background:linear-gradient(135deg,#f2f2f2,#cfcfcf 60%,#7a7470)" role="img" aria-label="Photo of a white entry hall with an open staircase"></div>
  <div class="abs gallery-item" style="left:376px;width:212px;background:linear-gradient(160deg,#b9b6b1,#ecebe8 55%,#d1cfcb)" role="img" aria-label="Photo of a white kitchen with a dining table"></div>
  <div class="abs gallery-item" style="left:610px;width:212px;background:linear-gradient(160deg,#d8d2c8,#efe9df 50%,#a89e92)" role="img" aria-label="Photo of a cream living room with curved sofa"></div>
  <div class="abs gallery-item" style="left:846px;width:212px;background:linear-gradient(135deg,#e9ebec,#c9ccce 55%,#8d8a86)" role="img" aria-label="Photo of a bright kitchen with stainless range"></div>
  <svg class="pager" style="top:3050px" viewBox="0 0 80 24" fill="none" stroke-width="1.5"><path d="M14 4 6 12l8 8M22 4l-8 8 8 8" stroke="#888"/><path d="M46 4l8 8-8 8M56 4l8 8-8 8M66 4l8 8-8 8" stroke="var(--accent)"/></svg>
</section>

<section aria-label="Team">
  <div class="abs team"></div>
  <h2 class="section-title" style="top:3241px">MEET OUR TEAM</h2>
  <div class="title-rule" style="top:3293px"></div>

  <div class="abs team-photo" style="left:141px;background:linear-gradient(135deg,#d9d4cd,#8a7560 55%,#b77d2e)" role="img" aria-label="Portrait of the president and CEO"></div>
  <div class="abs team-card" style="left:222px"><div class="team-name">DESMOND PRATT</div><div class="team-role">President &amp; CEO</div></div>

  <div class="abs team-photo" style="left:458px;background:linear-gradient(135deg,#7a5a42,#a08774 55%,#3e3a38)" role="img" aria-label="Portrait of the architect"></div>
  <div class="abs team-card" style="left:539px"><div class="team-name">VICTOR HALE</div><div class="team-role">Architect</div></div>

  <div class="abs team-photo" style="left:776px;background:linear-gradient(135deg,#f1f1f1,#dcdad8 55%,#2f2c2b)" role="img" aria-label="Portrait of the project manager"></div>
  <div class="abs team-card" style="left:857px"><div class="team-name">LENA MORROW</div><div class="team-role">Project Manager</div></div>
</section>

<footer class="abs site-footer"></footer>
<div class="abs foot-nav active" style="left:342px">HOME</div>
<div class="abs foot-nav" style="left:432px">ABOUT US</div>
<div class="abs foot-nav" style="left:550px">SERVICES</div>
<div class="abs foot-nav" style="left:661px">GALLERY</div>
<div class="abs foot-nav" style="left:770px">CONTACT US</div>
<div class="abs foot-rule" style="top:3800px"></div>

<div class="abs contact-col" style="left:200px;width:296px">
  <svg width="22" height="26" viewBox="0 0 22 26" fill="none" stroke="#fff" stroke-width="1.6"><path d="M11 24S3 15 3 9a8 8 0 0 1 16 0c0 6-8 15-8 15z"/><circle cx="11" cy="9" r="3"/></svg>
  <div style="margin-top:16px">123 Lorem ipsum dolor sit amet couer<br>adipiscing elit sed diam nonnmy.</div>
</div>
<div class="abs contact-divider" style="left:525px"></div>
<div class="abs contact-col" style="left:540px;width:180px">
  <svg width="26" height="26" viewBox="0 0 26 26" fill="none" stroke="#fff" stroke-width="1.6"><path d="M6 3l4 5-2 3c1 3 4 6 7 7l3-2 5 4-3 4C11 23 3 15 2 6z"/></svg>
  <div style="margin-top:12px"><strong>Phone:</strong><br>555-014-2298</div>
</div>
<div class="abs contact-divider" style="left:751px"></div>
<div class="abs contact-col" style="left:780px;width:270px">
  <svg width="28" height="26" viewBox="0 0 28 26" fill="none" stroke="#fff" stroke-width="1.6"><path d="M2 10 14 2l12 8v14H2z"/><path d="M2 10l12 9 12-9"/><path d="M7 7V4h14v3"/></svg>
  <div style="margin-top:12px"><strong>Email:</strong><br>info@clarabethholloway.example</div>
</div>

<div class="abs foot-rule" style="top:3942px"></div>
<div class="abs copyright">Copyright © 2020 <b>CLARA BETH HOLLOWAY.</b> All Rights Reserved.</div>
<div class="abs social" style="left:942px;background:#4a4f8f"></div>
<div class="abs social" style="left:973px;background:#b23a6a"></div>
<div class="abs social" style="left:1004px;background:#4a9ad4"></div>
<div class="abs social" style="left:1035px;background:#c9302c"></div>

</body>
</html>
```